Couples Workshop Flyer

I need a flyer to promote a one-day workshop for couples.

I am a therapist and life-coach and the session is called: "Lantern Bridge Days, and bring out the best in each other' - so Lantern Bridge Days is the bold name for the seminar but the point of the whole workshop is in the tagline, 'and bring out the best in each other'.

The final design should compel couples to take the risk to leave their comfort zones and attend a one-day workshop on a weekend .

Target Market(s)

Couples who are interested in self-improvement and identify with change and growth.
Somehow the flyer will match their aspirations!

Requirements
Should not have
• Not too many love hearts! :)
Not too gushy - a hint of romance!

```html
<!DOCTYPE html>
<html lang="en">
<head>
<meta charset="utf-8">
<title>Lantern Bridge Days – One-Day Couples Seminar</title>
<link href="https://fonts.googleapis.com/css2?family=Yesteryear&family=Rosarivo&family=Handlee&display=swap" rel="stylesheet">
<style>
  :root {
    --ink: #2b2b2b;
    --ink-soft: #444;
    --paper: #ffffff;
    --sky-top: #eef1f2;
    --sky-mid: #c9d3d6;
    --hill: #7f9a6a;
    --hill-dark: #4f6a3e;
    --ground: #8f8a78;
    --panel: rgba(255, 255, 255, 0.72);
    --frame: #d8d8d8;
  }
  * { box-sizing: border-box; margin: 0; padding: 0; }
  html, body { width: 900px; height: 1200px; overflow: hidden; background: var(--paper); }
  .flyer {
    position: relative;
    width: 900px;
    height: 1200px;
    overflow: hidden;
    color: var(--ink);
    background: var(--paper);
  }
  .scenery {
    position: absolute;
    left: 0; top: 520px;
    width: 900px; height: 680px;
    background:
      linear-gradient(to bottom, var(--paper) 0%, rgba(255,255,255,0) 32%),
      linear-gradient(to bottom, var(--sky-top) 0%, var(--sky-mid) 40%, var(--hill) 68%, var(--hill-dark) 86%, var(--ground) 100%);
  }
  .content { position: relative; z-index: 1; }
  .title {
    font-family: "Yesteryear", cursive;
    font-weight: 400;
    font-size: 92px;
    line-height: 1;
    text-align: center;
    padding-top: 34px;
    letter-spacing: 1px;
  }
  .tagline {
    font-family: "Rosarivo", serif;
    font-size: 36px;
    text-align: right;
    padding-right: 92px;
    margin-top: 6px;
  }
  .intro {
    font-family: "Rosarivo", serif;
    font-size: 18.5px;
    line-height: 1.45;
    margin: 40px 60px 0 66px;
    color: var(--ink-soft);
  }
  .gains {
    font-family: "Handlee", cursive;
    font-size: 16.5px;
    line-height: 1.38;
    margin: 30px 80px 0 88px;
    color: var(--ink-soft);
  }
  .gains-lead { margin-bottom: 14px; }
  .gains-list { list-style: none; padding-left: 20px; }
  .gains-list li {
    position: relative;
    padding-left: 18px;
    margin-bottom: 9px;
  }
  .gains-list li::before {
    content: "-";
    position: absolute;
    left: 0;
  }
  .cta {
    font-family: "Rosarivo", serif;
    font-size: 21px;
    text-align: center;
    line-height: 1.4;
    margin-top: 44px;
    color: var(--ink);
  }
  .presenter {
    position: absolute;
    left: 60px; top: 870px;
    width: 380px; height: 300px;
    background: var(--panel);
    z-index: 2;
    padding: 18px 18px 16px 18px;
    font-family: "Handlee", cursive;
    font-size: 13.5px;
    line-height: 1.35;
    color: var(--ink);
  }
  .presenter-photo {
    float: left;
    width: 74px; height: 96px;
    margin: 0 12px 6px 0;
    background: linear-gradient(#9bb3c6, #d9e2e8);
    border: 3px solid var(--paper);
    outline: 1px solid var(--frame);
  }
  .presenter-heading {
    font-family: "Yesteryear", cursive;
    font-weight: 400;
    font-size: 27px;
    line-height: 1;
    margin-bottom: 6px;
  }
  .presenter p + p { margin-top: 8px; clear: both; }
</style>
</head>
<body>
<div class="flyer">
  <div class="scenery" role="img" aria-label="Photo: a couple sitting close together on a grassy hillside, looking out over a misty mountain valley"></div>

  <div class="content">
    <h1 class="title">Lantern Bridge Days</h1>
    <p class="tagline">and bring out the best in each other</p>

    <p class="intro">Some couples spend up big on their wedding day but fail to invest in their marriage or relationship, but relationships take much more than love to be successful. This innovative one-day seminar helps couples to breathe new life into their relationship.</p>

    <div class="gains">
      <p class="gains-lead">What you will gain from Sam's seminar:</p>
      <ul class="gains-list">
        <li>How to turn an argument into a moment of closeness – Easier than you think!</li>
        <li>Know what stress is doing to your relating and the two skillsets will make a big difference to each other's stress-load.</li>
        <li>The role of pleasure in an emotionally-committed relationship and that's more than sex!</li>
        <li>Identify the traps of committed relationships – and why being in a relationship doesn't have to be a struggle.</li>
        <li>Learn how it's not you or your partner's fault – Identify the missing ingredients in relationship and what you can do to get these back.</li>
        <li>What the research says about the ingredients of great sex</li>
        <li>What to do about the three drains on your relationship: boredom, having nothing to say and those same-old arguments.</li>
        <li>You will also practice using Sam's negotiation tool that he developed for couples as well. Sam's seminars are fun, informative and practical.</li>
      </ul>
    </div>

    <p class="cta">Take your relationship to the next level and book your seat now:<br>http://www.samuelhartley.com.au/couples.html</p>
  </div>

  <aside class="presenter">
    <div class="presenter-photo" role="img" aria-label="Portrait photo of the presenter"></div>
    <h2 class="presenter-heading">About the presenter:</h2>
    <p>Samuel Hartley is a highly skilled couples therapist and educator who is known for his innovative and creative approaches in his work. He has appeared on Ch 4's Morning Brew show and Ch 6's Evening Desk as well as being interviewed on radio and in print.</p>
    <p>Sam's seminars are run along brain-based education principles he learnt from Dr Alan Merrow training in the USA, so that you will remember your new learning and integrate it into your life.</p>
  </aside>
</div>
</body>
</html>
```